Helicopter Tour Brochure Design (8.5 x 11" Bi-Fold Brochure)

Flyer Design for Helicopter Sightseeing Tours. Should be very inviting and touristy. Read "must have" section for more information.

Target Market(s)

Tourists visiting Florida

Industry/Entity Type

Aviation

Colors
3176b5
0456a4
85acd3
757575
9d9d9d
1b1b1b

Requirements
Must have
• Must include the Tour photos and "Route map", so customers know where the tours travels along. It must be inviting.
• Also, design must be for a 8.5 x 11" bi-fold brochure/flyer and include a brief description about our company:
• " Corvane Aviation offers unparalleled sightseeing opportunities with a commitment to safety & customer service. The view during our sightseeing tours will provide for your comfort & more beauty than you ever imagined. And like many of our customers, you’ll want to tell your friends all about it! Corvane Aviation’s experienced pilots will provide a comfortable flight leaving you with a smile on your face. Departure location will be the Pellmont Airport, unless otherwise requested with our office. "
• You can find the tour description online at www.corvanefly.com/tours, which should be included as well.
• Must be in PDF Format.
• 8.5 x 11" Bi-Fold Brochure
• ATTACHED ARE THE DETAILED FORMAT INFORMATION.

```html
<!DOCTYPE html>
<html lang="en">
<head>
<meta charset="utf-8">
<title>Corvane Aviation – Helicopter Sightseeing Tours</title>
<link rel="stylesheet" href="https://fonts.googleapis.com/css2?family=Arimo:wght@400;700&display=swap">
<style>
  :root {
    --backdrop: #d4d4d4;
    --sky-deep: #1f2f8c;
    --sky-mid: #2f48b0;
    --sky-light: #3176b5;
    --dusk-glow: #d98a78;
    --city-amber: #b9782e;
    --city-dark: #1b1b1b;
    --ink-white: #ffffff;
    --wedge: rgba(133, 172, 211, 0.22);
  }
  * { margin: 0; padding: 0; box-sizing: border-box; }
  html, body {
    width: 1200px; height: 960px; overflow: hidden;
    background: var(--backdrop);
    font-family: "Arimo", Arial, sans-serif;
  }
  .flyer {
    position: absolute; left: 40px; top: 50px;
    width: 1120px; height: 860px;
    overflow: hidden;
    box-shadow: 0 6px 24px rgba(0,0,0,0.25);
  }
  .flyer__photo {
    position: absolute; inset: 0;
    background:
      linear-gradient(180deg,
        var(--sky-deep) 0%,
        var(--sky-mid) 30%,
        var(--sky-light) 44%,
        var(--dusk-glow) 50%,
        #2a3a6a 54%,
        var(--city-amber) 72%,
        #4a3a2a 86%,
        var(--city-dark) 100%);
  }
  .flyer__wedge { position: absolute; inset: 0; }
  .brand {
    position: absolute; left: 70px; top: 70px;
    color: var(--ink-white);
    font-weight: 700; font-size: 40px; letter-spacing: 0.5px;
  }
  .contact {
    position: absolute; right: 70px; top: 66px;
    text-align: right; color: var(--ink-white);
    font-size: 20px; line-height: 1.3;
  }
  .headline {
    position: absolute; left: 330px; top: 470px;
    color: var(--ink-white);
    font-weight: 400; font-size: 92px; line-height: 0.98;
    letter-spacing: -1px;
    text-shadow: 0 2px 8px rgba(0,0,0,0.35);
  }
</style>
</head>
<body>
  <main class="flyer">
    <div class="flyer__photo" role="img" aria-label="Photo of a coastal city at dusk seen from above, deep blue cloudy sky over a sunset horizon and lit streets and buildings"></div>
    <svg class="flyer__wedge" width="1120" height="860" viewBox="0 0 1120 860" aria-hidden="true">
      <polygon points="1120,300 1120,860 640,860" fill="var(--wedge)"/>
      <polygon points="1120,120 1120,300 930,500" fill="rgba(255,255,255,0.10)"/>
    </svg>
    <div class="brand">Corvane Aviation</div>
    <address class="contact">
      +1 (555) 014 2260<br>
      info@corvanefly.com<br>
      corvanefly.com
    </address>
    <h1 class="headline">Helicopter<br>Sightseeing<br>Tours</h1>
  </main>
</body>
</html>
```